theater production in Seoul needs a poster of "Courtship Tutor: The Revue"

Title: "Courtship Tutor: The Revue"
Concept: This is a lively and fun musical centered around a dating coach who helps people navigate the ups and downs of modern romance. The show is full of humor, love, and the occasional heartache, highlighting the challenges of finding true love in today's world.
Visual Style: We are aiming for a vibrant and eye-catching design that captures the playful and romantic mood of the show. Think of bright colors, romantic symbols like hearts or arrows, and a modern urban setting. It should feel inviting, slightly humorous, and engaging.
Target Audience: Young adults and adults who enjoy romantic comedies and upbeat musicals. The tone should be fun and light, with a hint of romance.
Key Imagery: Possible elements could include a charismatic coach character holding a notepad or a whistle, silhouettes of couples, a city skyline in the background, or playful icons like phones, roses, and hearts. We want the poster to convey a sense of romance, excitement, and fun.

Text Elements:

Catchy tagline: "Finding love, one date at a time!"

Performance dates:2025. March 15_ May 31th
Sat. 1PM, Sun. 3pm, Wed/Fri 7:30pm

where:Hwasolgil Arthall
TICKET PRICE: $45
on the bottom side
Author Pyo Dain
Director-Gil Sorahm Composer_Moonbitnari
Producer_Ryu Donghwan Sound Director _Ahn Wol
actor_Tak Minjae Jeon Hyerin Nam Jiwoon Ha Boram Yeo Sanghun Cha Dohyeon

BOOK NOW
02 418-3956
PLUM COMPANY

```html
<!DOCTYPE html>
<html lang="en">
<head>
<meta charset="UTF-8">
<title>Courtship Tutor: The Revue</title>
<link href="https://fonts.googleapis.com/css2?family=Poiret+One&family=Montserrat:wght@400;500;600&display=swap" rel="stylesheet">
<style>
  :root{
    --ink:#0b0807;
    --night:#120d0b;
    --bar:#1c1a19;
    --ember:#f2a65a;
    --glow:#f7c98a;
    --rust:#7a3f1e;
    --white:#f4efe9;
    --muted:#a59a90;
  }
  *{margin:0;padding:0;box-sizing:border-box}
  html,body{width:847px;height:1200px;overflow:hidden;background:var(--ink)}
  .poster{
    position:relative;width:847px;height:1200px;overflow:hidden;
    background:var(--night);color:var(--white);
    font-family:"Montserrat",sans-serif;
  }
  .scene{
    position:absolute;left:0;top:0;width:847px;height:880px;
    background:
      radial-gradient(ellipse 300px 260px at 420px 420px, rgba(247,201,138,.95), rgba(242,166,90,.75) 35%, rgba(122,63,30,.55) 65%, transparent 100%),
      linear-gradient(180deg,#2a1a12 0%,#6b3a1c 30%,#a8602c 48%,#4a2a18 72%,var(--night) 100%);
  }
  .scene::before,.scene::after{
    content:"";position:absolute;top:0;bottom:0;width:190px;
    background:linear-gradient(90deg,var(--ink),rgba(11,8,7,.6) 60%,transparent);
  }
  .scene::before{left:0}
  .scene::after{right:0;transform:scaleX(-1)}
  .scene-fade{
    position:absolute;left:0;top:620px;width:847px;height:260px;
    background:linear-gradient(180deg,transparent,var(--night));
  }
  .tagline{
    position:absolute;left:0;top:36px;width:847px;text-align:center;
    font-family:"Poiret One",sans-serif;font-weight:400;font-size:80px;line-height:100px;
    letter-spacing:1px;text-transform:uppercase;color:var(--white);
  }
  .show-title{
    position:absolute;left:0;top:766px;width:847px;text-align:center;
    font-family:"Poiret One",sans-serif;font-weight:400;font-size:34px;line-height:40px;
    letter-spacing:4px;text-transform:uppercase;color:var(--glow);
  }
  .dates-label{
    position:absolute;top:834px;left:0;width:847px;text-align:center;
    font-size:11px;letter-spacing:5px;color:var(--muted);text-transform:uppercase;
  }
  .dates-box{
    position:absolute;left:122px;top:880px;width:605px;height:84px;
    border:1.5px solid var(--white);text-align:center;text-transform:uppercase;
  }
  .dates-box .range{margin-top:16px;font-size:15px;letter-spacing:2px;font-weight:500}
  .dates-box .times{margin-top:6px;font-size:23px;letter-spacing:1.5px;font-weight:500}
  .info{
    position:absolute;top:1000px;left:0;width:847px;display:flex;justify-content:center;gap:110px;
  }
  .info-item{display:flex;align-items:center;gap:12px}
  .info-item svg{width:22px;height:22px;flex:none}
  .info-item .label{font-size:11px;color:var(--muted);display:block}
  .info-item .value{font-size:17px;font-weight:500;display:block;margin-top:2px}
  .credits{
    position:absolute;top:1070px;left:0;width:847px;text-align:center;
    font-size:9.5px;letter-spacing:.6px;text-transform:uppercase;line-height:20px;color:var(--white);
  }
  .credits .role{color:var(--muted);margin-right:4px}
  .credits .sep{display:inline-block;width:14px}
  .booking{
    position:absolute;left:0;bottom:0;width:847px;height:60px;background:var(--bar);
    display:flex;align-items:center;justify-content:center;gap:10px;
    font-size:14px;letter-spacing:1px;font-weight:500;text-transform:uppercase;
  }
  .booking .company{margin-left:10px}
</style>
</head>
<body>
<main class="poster">
  <div class="scene" role="img" aria-label="Silhouette of a couple facing each other on a seaside rock beneath a glowing sunset, framed by dark cliffs"></div>
  <div class="scene-fade"></div>

  <p class="tagline">Finding love, one<br>date at a time!</p>

  <h1 class="show-title">Courtship Tutor: The Revue</h1>

  <p class="dates-label">Performance Dates</p>
  <section class="dates-box">
    <p class="range">2025. March 15_ May 31th</p>
    <p class="times">Sat. 1PM / Sun. 3PM / Wed/Fri 7:30PM</p>
  </section>

  <section class="info">
    <div class="info-item">
      <svg viewBox="0 0 24 24" fill="none" stroke="currentColor" stroke-width="1.8"><path d="M12 22s7-7 7-12a7 7 0 0 0-14 0c0 5 7 12 7 12z"/><circle cx="12" cy="10" r="2.5"/></svg>
      <div><span class="label">where:</span><span class="value">Hwasolgil Arthall</span></div>
    </div>
    <div class="info-item">
      <svg viewBox="0 0 24 24" fill="none" stroke="currentColor" stroke-width="1.8"><path d="M3 12V4h8l10 10-8 8z"/><circle cx="7.5" cy="8.5" r="1.5"/></svg>
      <div><span class="label">Ticket Price:</span><span class="value">$45</span></div>
    </div>
  </section>

  <section class="credits">
    <p><span class="role">Author</span>Pyo Dain<span class="sep"></span><span class="role">Director</span>Gil Sorahm<span class="sep"></span><span class="role">Composer</span>Moonbitnari<span class="sep"></span><span class="role">Producer</span>Ryu Donghwan<span class="sep"></span><span class="role">Sound Director</span>Ahn Wol</p>
    <p><span class="role">Actor</span>Tak Minjae, Jeon Hyerin, Nam Jiwoon, Ha Boram, Yeo Sanghun, Cha Dohyeon</p>
  </section>

  <footer class="booking">
    <span>Book now:</span><span>02 418-3956</span><span class="company">Plum Company</span>
  </footer>
</main>
</body>
</html>
```